Shift our Horizon the biggest community for CarbonOffset in the travel industry

We are a platform building a community for people to be able to measure and compensate carbon footprint. This community will be focused on Individuals and Businesses where they can measure their impact and choose projects to offset. I want to have a calculator of the number of kms being compensated as a community as well as the number of tons being removed. We are building the biggest community in the travel industry where users of Tours, Car Rentals, Events and eventually hotels will measure their footprint and contribute to a project to compensate and become part of the community to learn, connect and help with the environment. We will also invite companies to be part of the project so that they can offer this to their clients and employees.

Target Market(s)

At first travelers on holidays, business, events, conferences, tour operators. Next phase rental car companies, ride sharing apps

Industry/Entity Type

Travel

Number of Pages Required

1 page

Font styles to use
Serif
Sans Serif

Colors

Designer to choose colors to be used in the design.

Requirements
Must have
• A lot of images with an optimist focus. I want to stop the message that we are doomed and change it to we have an opportunity to do something, celebrate about that and build a community around this. It is intended for people between 25 - 50 years old. I want this project to be more human, our interaction and need to connect with nature. How it benefits us, etc.
Nice to have
• Videos of the projects, videos of people from the community sharing their thoughts. I am imagining somewhere within the webpage to have a mosaic with the pictures (from facebook if authorised by each person) to get and idea of how big the community is and put a human face.
Should not have
• Blaming messages of how the world will end, we have enough information on that.

```html
<!DOCTYPE html>
<html lang="en">
<head>
<meta charset="utf-8">
<title>Shift our Horizon – Carbon Calculator</title>
<link href="https://fonts.googleapis.com/css2?family=Oswald:wght@300;400;500&family=Josefin+Sans:wght@400;600;700&family=Arimo:wght@400;700&display=swap" rel="stylesheet">
<style>
:root{
  --green:#4dbb73;
  --green-soft:#6fcf95;
  --green-dark:#3a8c52;
  --brand:#4b7d55;
  --ink:#222;
  --grey-text:#666;
  --panel:#eeeeee;
  --tab:#f4f4f4;
  --footer:#1e1e1e;
  --white:#fff;
}
*{box-sizing:border-box;margin:0;padding:0}
html,body{width:1200px;height:3050px;overflow:hidden;background:var(--white)}
body{position:relative;font-family:"Josefin Sans",sans-serif;color:var(--ink)}
.abs{position:absolute}

/* header */
.site-header{position:absolute;left:0;top:0;width:1200px;height:123px;background:var(--white)}
.brand{position:absolute;left:40px;top:28px;display:flex;align-items:center;gap:12px}
.brand-dot{width:58px;height:58px;border-radius:50%;background:var(--brand)}
.brand-name{font-family:"Josefin Sans",sans-serif;font-weight:700;font-size:30px;color:var(--brand);line-height:1}
.main-nav{position:absolute;right:26px;top:86px;display:flex;font-family:"Oswald",sans-serif;font-weight:400;font-size:17px;color:#666;letter-spacing:.3px}
.main-nav span{padding:0 18px;border-right:1.5px solid #888;line-height:18px}
.main-nav span:last-child{border-right:none;padding-right:0}

/* hero */
.hero{position:absolute;left:0;top:123px;width:1200px;height:640px}
.hero-photo{position:absolute;inset:0;background:linear-gradient(180deg,#c9c6a6 0%,#9aa27a 25%,#7b7a55 45%,#8e8a5a 60%,#6f8b35 80%,#5e7c2c 100%)}
.hero-counter{position:absolute;right:30px;top:28px;font-family:"Arimo",sans-serif;font-weight:700;font-size:18px;color:#333}
.hero-title{position:absolute;left:41px;top:125px;font-family:"Oswald",sans-serif;font-weight:500;font-size:52px;color:var(--white);letter-spacing:.5px}
.hero-sub{position:absolute;left:41px;top:186px;font-family:"Oswald",sans-serif;font-weight:300;font-size:29px;line-height:41px;color:var(--white)}
.hero-dots{position:absolute;left:565px;top:562px;display:flex;gap:5px}
.hero-dots i{width:14px;height:14px;border-radius:50%;background:#d8d8d8}

/* guide */
.guide-photo-shadow{position:absolute;left:97px;top:855px;width:463px;height:328px;background:#1d1d1d}
.guide-photo{position:absolute;left:107px;top:865px;width:478px;height:338px;background:radial-gradient(circle at 55% 45%,#6b5a3c 0%,#8aa24e 35%,#74a13a 70%,#4f7d25 100%);box-shadow:0 4px 12px rgba(0,0,0,.25)}
.guide-title{position:absolute;left:635px;top:890px;font-family:"Oswald",sans-serif;font-weight:400;font-size:34px;color:#333}
.guide-text{position:absolute;left:635px;top:958px;width:470px;font-size:19px;line-height:25px;color:#333}
.guide-text .link{color:var(--green)}
.btn-read{position:absolute;left:651px;top:1130px;width:128px;height:58px;background:var(--green-soft);color:var(--white);font-size:20px;display:flex;align-items:center;justify-content:center;border-radius:3px}

/* calculator */
.calc-panel{position:absolute;left:0;top:1257px;width:1200px;height:850px;background:var(--panel)}
.calc-card{position:absolute;left:24px;top:1330px;width:1152px;height:755px;background:var(--white)}
.type-tabs{position:absolute;left:24px;top:1273px;width:1152px;height:40px;display:flex;font-family:"Arimo",sans-serif;font-weight:700;font-size:19px;color:#444}
.type-tabs span{display:flex;align-items:center;justify-content:center;background:var(--tab);border:1px solid #ddd;border-left:none}
.type-tabs .active{background:#d6ddd4;color:#4a6e55;border-left:1px solid #ddd}
.step-tabs{position:absolute;left:24px;top:1334px;width:1152px;height:46px;border-bottom:3px solid var(--green)}
.step-tabs span{position:absolute;top:6px;font-size:22px;color:var(--green-soft)}
.step-tabs .active{top:0;left:140px;width:132px;height:43px;background:var(--green);color:var(--white);display:flex;align-items:center;justify-content:center;border-radius:14px 0 0 0;clip-path:polygon(8% 0,92% 0,100% 100%,0 100%)}
.calc-icon{position:absolute;left:53px;top:1414px;width:112px;height:121px;background:linear-gradient(135deg,#6ab544,#3f8c2a)}
.calc-heading{position:absolute;left:198px;top:1420px;font-family:"Arimo",sans-serif;font-weight:700;font-size:26px;color:var(--green)}
.calc-intro{position:absolute;left:198px;top:1455px;width:900px;font-size:21px;line-height:30px;color:#222}
.calc-intro .hint{color:var(--green)}
.calc-rule{position:absolute;left:57px;top:1571px;width:1090px;height:1px;background:#ddd}
.people{position:absolute;left:190px;top:1601px;font-weight:700;font-size:23px;color:var(--green);display:flex;align-items:center;gap:14px}
.select-small{width:60px;height:28px;border:1px solid #ccc;border-radius:3px;position:relative;font-weight:400;color:#222;font-size:20px;padding:4px 12px}
.spin{position:absolute;right:0;top:0;width:24px;height:100%;background:var(--green);border-radius:0 3px 3px 0}
.spin::before,.spin::after{content:"";position:absolute;left:8px;width:6px;height:6px;border-left:2px solid #fff;border-top:2px solid #fff}
.spin::before{top:6px;transform:rotate(45deg)}
.spin::after{bottom:6px;transform:rotate(225deg)}
.row{position:absolute;left:190px;height:40px;display:flex;align-items:center;font-size:22px;color:var(--green-dark)}
.row .label{width:202px}
.field{width:143px;height:38px;border:1px solid #ddd;position:relative}
.row .unit{margin-left:18px}
.row .field.second{margin-left:18px}
.btn-calc{position:absolute;left:943px;top:2045px;width:205px;height:40px;background:var(--green-soft);color:#24683a;font-family:"Arimo",sans-serif;font-weight:700;font-size:19px;display:flex;align-items:center;justify-content:center;clip-path:polygon(6% 0,94% 0,100% 100%,0 100%)}

/* offsetting */
.offset-title{position:absolute;left:0;width:1200px;top:2170px;text-align:center;font-family:"Oswald",sans-serif;font-size:35px;color:#333}
.offset-title span{border-bottom:2px solid #333;padding-bottom:2px}
.offset-text{position:absolute;left:0;width:1200px;top:2238px;text-align:center;font-size:20px;line-height:26px;color:#333}
.tile{position:absolute;top:2325px;width:190px;height:190px;border-radius:50%;overflow:hidden}
.tile-label{position:absolute;left:0;right:0;bottom:0;height:64px;background:rgba(40,40,40,.55);color:#fff;font-family:"Arimo",sans-serif;font-weight:700;font-size:19px;line-height:22px;text-align:center;padding-top:8px}
.arrow{position:absolute;top:2408px;width:14px;height:14px;border-left:3px solid #777;border-top:3px solid #777}

/* footer */
.site-footer{position:absolute;left:0;top:2580px;width:1200px;height:470px}
.foot-head{position:absolute;font-family:"Oswald",sans-serif;font-weight:400;font-size:20px;color:#ddd}
.foot-list{position:absolute;font-family:"Oswald",sans-serif;font-weight:300;font-size:15.5px;line-height:25px;color:#eee;list-style:none}
.newsletter{position:absolute;left:850px;top:2794px;width:239px;height:47px;border:2px solid #eee;color:#eee;font-family:"Arimo",sans-serif;font-size:11px;display:flex;align-items:center;justify-content:space-between;padding:0 16px}
.social{position:absolute;top:2870px;width:35px;height:35px;border:2px solid #eee;border-radius:50%}
.foot-rule{position:absolute;left:108px;top:2982px;width:983px;height:1px;background:#555}
.copyright{position:absolute;left:0;width:1200px;top:3010px;text-align:center;font-family:"Arimo",sans-serif;font-size:12px;color:#ddd}
</style>
</head>
<body>

<header class="site-header">
  <div class="brand"><div class="brand-dot"></div><div class="brand-name">Shift our Horizon</div></div>
  <nav class="main-nav">
    <span>CALCULATE</span><span>OFFSETTING</span><span>BUSINESSES</span><span>INFORMATION</span><span>ABOUT US</span><span>CONTACT</span><span>SEARCH</span>
  </nav>
</header>

<section class="hero">
  <div class="hero-photo" role="img" aria-label="Hiker with a backpack and a dog on a grassy hilltop overlooking a lake and hills at sunrise"></div>
  <div class="hero-counter">798,264 kms we as a community have to offset together &rsaquo;</div>
  <h1 class="hero-title">CARBON CALCULATOR</h1>
  <p class="hero-sub">Show you care for the environment and<br>communities by by Carbon Offsetting &gt;</p>
  <div class="hero-dots"><i></i><i></i><i></i><i></i></div>
  <svg class="abs" style="left:0;top:470px" width="1200" height="170" viewBox="0 0 1200 170">
    <path d="M0 155 L0 120 C250 190 600 170 900 110 C1040 80 1140 55 1200 40 L1200 170 Z" fill="#fff"/>
    <path d="M0 120 C250 190 600 170 900 110 C1040 80 1140 55 1200 40" fill="none" stroke="#b9b9b9" stroke-width="14"/>
    <path d="M0 100 C60 130 120 145 200 155" fill="none" stroke="#b9b9b9" stroke-width="10"/>
  </svg>
</section>

<section class="guide">
  <div class="guide-photo-shadow"></div>
  <div class="guide-photo" role="img" aria-label="Hand holding a small seedling in soil against a green background"></div>
  <h2 class="guide-title">CARBON FOOTPRINTING GUIDE...</h2>
  <p class="guide-text">A <span class="link">carbon footprint</span> measures the total greenhouse gas emissions caused directly and indirectly by a person, organisation, event or product. It is measured in tonnes of carbon dioxide equivalent (tCO2e). Greenhouse gases can be compared on a like-for-like basis relative to one unit of CO2...</p>
  <div class="btn-read">Read More</div>
</section>

<section class="calculator">
  <div class="calc-panel"></div>
  <div class="type-tabs">
    <span class="active" style="width:173px">INDIVIDUAL</span>
    <span style="width:238px">TRAVEL / HOLIDAY</span>
    <span style="width:249px">TOUR OPERATORS</span>
    <span style="width:189px">BUSINESS</span>
    <span style="width:152px">EVENTS</span>
    <span style="width:151px">OTHER</span>
  </div>
  <div class="calc-card"></div>
  <div class="step-tabs">
    <span style="left:22px">Welcome</span>
    <span class="active">House</span>
    <span style="left:292px">Flights</span>
    <span style="left:411px">Car</span>
    <span style="left:505px">Motorbike</span>
    <span style="left:666px">Rail / Bus</span>
    <span style="left:820px">Secondary</span>
    <span style="left:986px">RESULTS</span>
  </div>
  <div class="calc-icon" role="img" aria-label="Water droplets on a green leaf"></div>
  <h3 class="calc-heading">HOUSEHOLD CARBON FOOTPRINT CALCULATOR</h3>
  <p class="calc-intro">Enter your consumption of each type of energy, and press the Calculate button<br>Your individual footprint is calculated by dividing the amount of energy by the<br>number of people in your house. <span class="hint">To calculate your full household footprint, select "1".</span></p>
  <div class="calc-rule"></div>
  <div class="people">How many people are in your house? <div class="select-small">1<span class="spin"></span></div></div>

  <div class="row" style="top:1654px"><span class="label">Electricity:</span><div class="field"><span class="spin"></span></div><span class="unit">kWh at a factor of</span><div class="field second"><span class="spin"></span></div></div>
  <div class="row" style="top:1714px"><span class="label">Natural Gas:</span><div class="field"><span class="spin"></span></div><span class="unit">therms</span></div>
  <div class="row" style="top:1774px"><span class="label">Heating Oil:</span><div class="field"><span class="spin"></span></div><span class="unit">US Gallons</span></div>
  <div class="row" style="top:1834px"><span class="label">Coal:</span><div class="field"><span class="spin"></span></div><span class="unit">kWh</span></div>
  <div class="row" style="top:1894px"><span class="label">LPG:</span><div class="field"><span class="spin"></span></div><span class="unit">therms</span></div>
  <div class="row" style="top:1954px"><span class="label">Propane:</span><div class="field"><span class="spin"></span></div><span class="unit">US Gallons</span></div>
  <div class="row" style="top:2014px"><span class="label">Wooden Pellets:</span><div class="field"><span class="spin"></span></div><span class="unit">metric tons</span></div>
  <div class="btn-calc">CALCULATE</div>
</section>

<section class="offsetting">
  <h2 class="offset-title"><span>WHAT IS CARBON OFFSETTING?</span></h2>
  <p class="offset-text">Being ‘carbon neutral’ is the ultimate goal towards preventing climate change.<br>It’s where your carbon output is effectively reduced to zero.</p>
  <div class="arrow" style="left:34px;transform:rotate(-45deg)"></div>
  <div class="tile" style="left:65px;background:radial-gradient(circle,#6f9a3a,#4a3524 70%)" role="img" aria-label="Hands holding a seedling in a soil pot"><div class="tile-label">Planting<br>trees</div></div>
  <div class="tile" style="left:281px;background:linear-gradient(180deg,#b8d77d,#4f8a2e)" role="img" aria-label="Sunlit green forest"><div class="tile-label">Protecting<br>forests</div></div>
  <div class="tile" style="left:506px;background:radial-gradient(circle at 60% 50%,#5f8c3a,#cfe0b5 70%)" role="img" aria-label="Hand planting a young tree"><div class="tile-label">Carbon<br>credits</div></div>
  <div class="tile" style="left:723px;background:linear-gradient(160deg,#4e7b2b,#6b2431 50%,#e0772c)" role="img" aria-label="Fresh beetroot and carrots from a garden"><div class="tile-label">Grow your<br>own</div></div>
  <div class="tile" style="left:940px;background:radial-gradient(circle at 55% 45%,#5e4a35,#8fc057 55%,#5b8f2d)" role="img" aria-label="Hand holding a seedling in soil"><div class="tile-label">Carbon<br>offset</div></div>
  <div class="arrow" style="left:1158px;transform:rotate(135deg)"></div>
</section>

<footer class="site-footer">
  <svg class="abs" style="left:0;top:0" width="1200" height="470" viewBox="0 0 1200 470">
    <path d="M0 58 C300 -10 620 40 900 80 C1040 95 1130 70 1200 40 L1200 470 L0 470 Z" fill="#1e1e1e"/>
    <path d="M0 58 C300 -10 620 40 900 80 C1040 95 1130 70 1200 40" fill="none" stroke="#8cc63f" stroke-width="8"/>
  </svg>
</footer>
<div class="foot-head" style="left:47px;top:2668px">Carbon Offsetting:</div>
<ul class="foot-list" style="left:63px;top:2720px">
  <li>Carbon neutral</li><li>Carbon offsets</li><li>Verified Carbon Standard</li><li>Gold Standard</li><li>Certified Emission Reduction</li><li>Quality Assurance Standard</li><li>Carbon offsetting</li>
</ul>
<div class="foot-head" style="left:288px;top:2668px">Consultancy:</div>
<ul class="foot-list" style="left:303px;top:2720px">
  <li>Carbon and GHG management</li><li>Verification and Assurance</li><li>Energy Management</li><li>Mandatory</li><li>Support</li><li>H&amp;S Systems</li><li>Lifecycle Assessments (LCA)</li>
</ul>
<div class="foot-head" style="left:848px;top:2736px">Newsletter:</div>
<div class="newsletter"><span>Enter The Email</span><span style="font-size:16px">&rarr;</span></div>
<div class="social" style="left:849px"></div>
<div class="social" style="left:896px"></div>
<div class="social" style="left:943px"></div>
<div class="foot-rule"></div>
<div class="copyright">Copyrights © 2019.All rights reserved. Terms | Privacy</div>

</body>
</html>
```